Flatscorehub Card

I need a new, trendy design for an Apartment Rating card that we hand out to residents at our apartments asking them to give us a review. Attached is what we currently hand out, but I need the new one to have a general picture or graphic that is fun and modern.
I need a new headline, use your imagination, but here are a few I like:
Be a Not-So-Secret Admirer
Love Us/Rate Us/Share Us
Copy:
Thank you for your recent visit to our office. We want to provide you with +1 Customer Service. Would you consider posting a review of us online? in addition to providing feedback, online reviews can help other customers learn about who we are and reviews are a great way to give a referral to your family and friends.
Please include the following logos:
Flatscorehub.net
Chatterloop
Zendro Business
Vantly
Be creative and add anything you have seen to help us stand out.
Target Market(s)
Resident who live at our apartment communities and potential renters.
Industry/Entity Type
Real Estate
Colors
Designer to choose colors to be used in the design.
Look and feel

```html
<!DOCTYPE html>
<html lang="en">
<head>
<meta charset="utf-8">
<title>Be a Not-So-Secret Admirer – Review Card</title>
<link href="https://fonts.googleapis.com/css2?family=Lato:ital,wght@0,400;0,700;0,900;1,400;1,700&family=Kalam:wght@700&family=Varela+Round&display=swap" rel="stylesheet">
<style>
  :root {
    --page-bg: #dcdcdf;
    --brand-blue: #2c5597;
    --ink-dark: #1d1d1f;
    --teal: #0f5f78;
    --teal-deep: #0b4d63;
    --teal-strip: #0d6f88;
    --orange: #e08a14;
    --tile-blue: #1f86cf;
    --tile-red: #c9201d;
    --white: #ffffff;
  }
  * { box-sizing: border-box; margin: 0; padding: 0; }
  html, body { width: 1200px; height: 1200px; overflow: hidden; background: var(--page-bg); }
  .card {
    position: absolute; left: 200px; top: 0;
    width: 800px; height: 1200px; overflow: hidden;
    background: var(--teal);
    font-family: "Lato", sans-serif; color: var(--white);
  }
  .hero-photo {
    position: absolute; left: 0; top: 0; width: 800px; height: 640px;
    background:
      radial-gradient(ellipse 220px 320px at 610px 420px, #3a3b3d 0%, #3a3b3d 55%, rgba(58,59,61,0) 100%),
      linear-gradient(180deg, #f4f4f4 0%, #e6e6e6 28%, #9a9a9a 45%, #5e5e5e 62%, #3d3d3d 82%, #2a2a2a 100%);
  }
  .brand {
    position: absolute; left: 58px; top: 72px;
    display: flex; align-items: center; gap: 18px;
  }
  .brand-mark { width: 72px; height: 72px; background: var(--brand-blue); border-radius: 6px; }
  .brand-name {
    font-family: "Varela Round", sans-serif; font-weight: 400;
    font-size: 48px; color: var(--brand-blue); letter-spacing: 0.5px;
  }
  .headline {
    position: absolute; left: 74px; top: 322px;
    font-weight: 900; font-size: 49px; line-height: 61px;
    text-transform: uppercase; letter-spacing: -0.5px;
    text-shadow: 0 2px 6px rgba(0,0,0,0.45);
  }
  .wave { position: absolute; left: 0; top: 530px; width: 800px; height: 140px; }
  .thanks {
    position: absolute; left: 75px; top: 646px;
    font-family: "Kalam", cursive; font-weight: 700; font-size: 42px;
  }
  .message {
    position: absolute; left: 74px; top: 722px; width: 652px;
    font-style: italic; font-size: 23px; line-height: 30px;
    text-align: justify; letter-spacing: -0.3px;
  }
  .review-sites {
    position: absolute; left: 125px; top: 920px;
    display: flex; gap: 31px;
  }
  .site-tile {
    width: 107px; height: 107px; border-radius: 10px;
    border: 2px solid rgba(255,255,255,0.85);
    display: flex; align-items: center; justify-content: center; text-align: center;
    font-weight: 700; font-size: 15px; line-height: 18px; color: var(--white);
    padding: 6px;
  }
  .site-tile--ratings { background: var(--tile-blue); }
  .site-tile--zendro, .site-tile--vantly { background: var(--tile-red); }
  .compliance {
    position: absolute; left: 594px; top: 958px;
    display: flex; gap: 20px; align-items: flex-end;
  }
  .footer-band {
    position: absolute; left: 0; top: 1055px; width: 800px; height: 115px;
    background: var(--orange); text-align: center;
    font-size: 24px; line-height: 31px; padding-top: 30px; letter-spacing: -0.2px;
  }
  .footer-strip { position: absolute; left: 0; top: 1170px; width: 800px; height: 30px; background: var(--teal-strip); }
</style>
</head>
<body>
  <main class="card">
    <div class="hero-photo" role="img" aria-label="Black and white city skyline with a smiling professional woman in a dark blazer, arms crossed"></div>

    <div class="brand">
      <span class="brand-mark"></span>
      <span class="brand-name">Flatscorehub</span>
    </div>

    <h1 class="headline">Be a<br>Not-so-secret<br>Admirer</h1>

    <svg class="wave" viewBox="0 0 800 140" preserveAspectRatio="none" aria-hidden="true">
      <path d="M0 30 C150 -10 260 10 400 40 C540 70 650 70 800 40 L800 140 L0 140 Z" fill="#1d1d1f"/>
      <path d="M0 80 C180 40 300 50 420 80 C560 115 680 110 800 70 L800 140 L0 140 Z" fill="#0f5f78"/>
    </svg>

    <h2 class="thanks">Thank you...</h2>
    <p class="message">For your recent visit to our office. We want to provide you with +1 Customer Service. Would you consider posting a review of us online? in addition to providing feedback, online reviews can help other customers learn about who we are and reviews are a great way to give a referral to your family and friends.</p>

    <div class="review-sites">
      <div class="site-tile site-tile--ratings">Flatscorehub.net</div>
      <div class="site-tile site-tile--zendro">Zendro Business</div>
      <div class="site-tile site-tile--vantly">Vantly</div>
    </div>

    <div class="compliance" aria-label="Accessible and fair housing">
      <svg width="54" height="62" viewBox="0 0 54 62" fill="none" stroke="#e08a14" stroke-width="4" stroke-linecap="round" aria-hidden="true">
        <circle cx="16" cy="6" r="4"/>
        <path d="M16 14 L18 34 L36 34 L44 54"/>
        <path d="M17 24 L32 24"/>
        <path d="M12 30 A16 16 0 1 0 34 50"/>
      </svg>
      <svg width="60" height="54" viewBox="0 0 60 54" fill="none" stroke="#e08a14" stroke-width="5" aria-hidden="true">
        <rect x="6" y="6" width="48" height="44"/>
      </svg>
    </div>

    <footer class="footer-band">
      <p>1420 Willow Crest Ave, Fairmont, NE 68599 | (402) 555-0148</p>
      <p>www.livemaplecourtapts.com</p>
    </footer>
    <div class="footer-strip"></div>
  </main>
</body>
</html>
```